Business card design for international hub site

I need a business card design with the logo attached. Although the site is for the teenage audience (it is about the high school graduation ball, the Prom), the business card is for professional use to be given to professional contacts (B2B), such as suppliers and partners, so it needs to look professional (but also girly, glamours and clean).

Target Market(s)

B2B

Industry/Entity Type

Media

Colors
eea4c8
f9d9e8
e667a6
9d9d9d
1b1b1b

Requirements
Must have
• Space for Name, Tile, Address, Phone, email and website.
Should not have
• Photo

```html
<!DOCTYPE html>
<html lang="en">
<head>
<meta charset="utf-8">
<title>The Dance Hive — Business Card</title>
<link rel="stylesheet" href="https://fonts.googleapis.com/css2?family=EB+Garamond:ital,wght@0,400;0,500;0,700;1,400&display=swap">
<style>
  :root {
    --pink: #e667a6;
    --pink-soft: #eea4c8;
    --blush: #f9d9e8;
    --grey: #9d9d9d;
    --grey-dark: #8a8b8d;
    --ink: #1b1b1b;
    --paper: #ffffff;
    --backdrop: #a7a7a7;
  }
  * { margin: 0; padding: 0; box-sizing: border-box; }
  html, body { width: 1200px; height: 1200px; overflow: hidden; }
  body {
    background: var(--backdrop);
    font-family: "EB Garamond", Georgia, serif;
    color: var(--ink);
    position: relative;
  }
  .card {
    position: absolute;
    left: 120px;
    width: 960px;
    height: 544px;
    background: var(--paper);
    overflow: hidden;
    box-shadow: 0 6px 18px rgba(0,0,0,0.22);
  }
  .card--front { top: 40px; }
  .card--back { top: 616px; }
  .card__waves { position: absolute; inset: 0; width: 100%; height: 100%; }

  .brand-name {
    position: absolute;
    color: var(--pink);
    font-weight: 500;
    line-height: 1;
    white-space: nowrap;
  }
  .card--front .brand-name { left: 78px; top: 150px; font-size: 60px; }
  .card--back .brand-name { left: 0; right: 0; top: 196px; text-align: center; font-size: 92px; }

  .address {
    position: absolute;
    left: 78px; top: 376px;
    font-size: 27px;
    line-height: 1.2;
  }
  .person {
    position: absolute;
    right: 46px; top: 132px;
    text-align: right;
  }
  .person__name { font-size: 35px; font-weight: 700; line-height: 1; }
  .person__title { font-size: 24px; font-style: italic; line-height: 1.1; }

  .contacts {
    position: absolute;
    right: 44px; top: 238px;
    list-style: none;
    text-align: right;
    font-size: 25px;
    line-height: 37px;
  }
  .contacts li { display: flex; justify-content: flex-end; align-items: center; gap: 10px; }
  .contacts svg { width: 26px; height: 26px; flex: none; }

  .website {
    position: absolute;
    right: 28px; bottom: 16px;
    color: var(--paper);
    font-size: 27px;
    font-weight: 700;
  }
</style>
</head>
<body>

<section class="card card--front" aria-label="Business card front">
  <svg class="card__waves" viewBox="0 0 960 544" preserveAspectRatio="none" aria-hidden="true">
    <path fill="var(--grey-dark)" d="M550 474 Q 820 456 960 396 L960 428 Q 820 476 550 478 Z"/>
    <path fill="var(--pink)" d="M0 486 L 520 486 Q 830 480 960 434 L960 544 L0 544 Z"/>
  </svg>

  <p class="brand-name">the dance hive</p>

  <p class="address">Unit, Street,<br>City, State, Zip</p>

  <div class="person">
    <p class="person__name">Name Here</p>
    <p class="person__title">Title</p>
  </div>

  <ul class="contacts">
    <li>(000) 000-0000
      <svg viewBox="0 0 26 26" aria-hidden="true"><circle cx="13" cy="13" r="13" fill="var(--ink)"/><rect x="9" y="6" width="8" height="14" rx="1.5" fill="var(--paper)"/><rect x="10.5" y="8" width="5" height="8" fill="var(--ink)"/></svg>
    </li>
    <li>(000) 000-0000
      <svg viewBox="0 0 26 26" aria-hidden="true"><circle cx="13" cy="13" r="13" fill="var(--ink)"/><path d="M7 11 Q13 5 19 11 L17 13 L15 11 L11 11 L9 13 Z" fill="var(--paper)"/><rect x="9" y="13" width="8" height="6" rx="1" fill="var(--paper)"/></svg>
    </li>
    <li>name@thedancehive.com
      <svg viewBox="0 0 26 26" aria-hidden="true"><circle cx="13" cy="13" r="13" fill="var(--ink)"/><rect x="6.5" y="8.5" width="13" height="9" fill="none" stroke="var(--paper)" stroke-width="1.8"/><path d="M6.5 8.5 L13 14 L19.5 8.5" fill="none" stroke="var(--paper)" stroke-width="1.8"/></svg>
    </li>
    <li>profiles.net/in/name
      <svg viewBox="0 0 26 26" aria-hidden="true"><circle cx="13" cy="13" r="13" fill="var(--ink)"/><rect x="5.5" y="10" width="9" height="6" rx="3" fill="none" stroke="var(--paper)" stroke-width="1.8"/><rect x="11.5" y="10" width="9" height="6" rx="3" fill="none" stroke="var(--paper)" stroke-width="1.8"/></svg>
    </li>
  </ul>

  <p class="website">www.thedancehive.com</p>
</section>

<section class="card card--back" aria-label="Business card back">
  <svg class="card__waves" viewBox="0 0 960 544" preserveAspectRatio="none" aria-hidden="true">
    <path fill="var(--grey-dark)" d="M550 474 Q 820 456 960 396 L960 428 Q 820 476 550 478 Z"/>
    <path fill="var(--pink)" d="M0 486 L 520 486 Q 830 480 960 434 L960 544 L0 544 Z"/>
  </svg>

  <p class="brand-name">the dance hive</p>
</section>

</body>
</html>
```